Postcard Design

www.lirvo.com.au
i am an occupational therapist and professionally trained coach. i work with children, parents and disability service providers to achieve brilliant outcomes for children with special needs.
http://www.lirvo.com.au/service/for-families
I need a postcard to give parents to promote our family service coaching service
A family service coach will work with you to set specific goals for your child, build a dream team, design and manage your child's highly effective therapy and educational team to ensure brilliant outcomes for your child..
KORLU - you have done my business card previously. they were great thank you.

```html
<!DOCTYPE html>
<html lang="en">
<head>
<meta charset="utf-8">
<title>Family Service Coaching Postcard</title>
<link href="https://fonts.googleapis.com/css2?family=Arimo:wght@400;700&family=Lato:wght@400;700&display=swap" rel="stylesheet">
<style>
  :root {
    --stage: #3a3a3c;
    --blue: #4a72bd;
    --blue-deep: #3f63ad;
    --lavender: #8e9fd8;
    --lavender-pale: #c4cbea;
    --ring: #b4c0e6;
    --teal: #5cc2c4;
    --navy: #1f2f5c;
    --ink: #2a3354;
    --white: #ffffff;
  }
  * { box-sizing: border-box; margin: 0; padding: 0; }
  html, body { width: 1172px; height: 1200px; overflow: hidden; background: var(--stage); }
  .canvas { position: relative; width: 1172px; height: 1200px; }

  .card { position: absolute; left: 66px; width: 1040px; height: 504px; overflow: hidden; background: var(--white); box-shadow: 0 4px 14px rgba(0,0,0,.35); }
  .card--front { top: 54px; }
  .card--back { top: 636px; }
  .card__art { position: absolute; inset: 0; width: 1040px; height: 504px; display: block; }

  .front__title { position: absolute; left: 57px; top: 46px; font: 700 33px/1 "Arimo", Arial, sans-serif; color: var(--white); letter-spacing: .3px; }
  .front__question { position: absolute; left: 53px; top: 100px; font: 400 29px/1 "Lato", sans-serif; color: var(--teal); }
  .front__pill { position: absolute; left: 48px; top: 157px; width: 560px; height: 38px; border-radius: 19px; background: var(--white); border: 3px solid var(--lavender); box-shadow: 0 0 0 3px var(--blue-deep); }
  .front__pill span { display: block; padding-left: 16px; font: 700 24px/32px "Lato", sans-serif; color: var(--navy); }

  .benefits { position: absolute; top: 215px; list-style: none; width: 262px; }
  .benefits--left { left: 53px; }
  .benefits--right { left: 324px; width: 280px; }
  .benefits li { position: relative; padding-left: 14px; font: 400 13.5px/1.2 "Lato", sans-serif; color: var(--white); margin-bottom: 5px; }
  .benefits li::before { content: ""; position: absolute; left: 0; top: 5px; width: 6px; height: 6px; border-radius: 50%; background: #c9d2f0; }

  .contact { position: absolute; font-family: "Arimo", Arial, sans-serif; color: var(--navy); }
  .contact__cta { font: 700 13.5px/1 "Lato", sans-serif; color: var(--teal); letter-spacing: .4px; margin-bottom: 8px; }
  .contact__row { display: flex; align-items: center; gap: 6px; }
  .contact__row svg { width: 14px; height: 14px; flex: none; }
  .contact__phone { font-size: 22px; line-height: 28px; }
  .contact__small { font-size: 15px; line-height: 20px; }
  .card--front .contact { left: 54px; top: 371px; }
  .card--back .contact { left: 408px; top: 388px; }

  .brand { position: absolute; display: flex; align-items: center; gap: 12px; }
  .brand__dot { width: 40px; height: 40px; border-radius: 50%; background: var(--blue); }
  .brand__name { font: 400 38px/1 "Lato", sans-serif; color: var(--blue); }
  .card--front .brand { left: 255px; top: 410px; }
  .card--back .brand { left: 630px; top: 410px; }

  .bio { position: absolute; left: 407px; top: 178px; width: 600px; font: 400 16.5px/1.27 "Lato", sans-serif; color: var(--ink); text-align: justify; }
  .bio p + p { margin-top: 9px; }
</style>
</head>
<body>
<main class="canvas">

  <section class="card card--front" aria-label="Postcard front">
    <svg class="card__art" viewBox="0 0 1040 504" aria-hidden="false">
      <defs>
        <linearGradient id="familyTone" x1="0" y1="0" x2="1" y2="1">
          <stop offset="0" stop-color="#e9e2d4"/>
          <stop offset=".5" stop-color="#d8b9a2"/>
          <stop offset="1" stop-color="#7d95b8"/>
        </linearGradient>
        <linearGradient id="childTone" x1="0" y1="0" x2="0" y2="1">
          <stop offset="0" stop-color="#8aa36a"/>
          <stop offset=".6" stop-color="#e2bca6"/>
          <stop offset="1" stop-color="#d77f93"/>
        </linearGradient>
      </defs>
      <rect width="1040" height="504" fill="var(--white)"/>
      <path d="M0,0 H1040 V420 C820,440 560,330 300,330 C180,330 80,338 0,345 Z" fill="var(--blue)"/>
      <path d="M0,345 C80,338 180,330 300,330 C560,330 820,440 1040,420 V445 C820,465 560,355 300,352 C180,350 80,356 0,362 Z" fill="var(--lavender)"/>
      <circle cx="837" cy="160" r="226" fill="var(--ring)"/>
      <circle cx="837" cy="160" r="210" fill="url(#familyTone)" role="img" aria-label="Photo of a smiling family with young children"/>
      <circle cx="891" cy="333" r="110" fill="var(--ring)"/>
      <circle cx="891" cy="333" r="98" fill="url(#childTone)" role="img" aria-label="Photo of a smiling young girl"/>
    </svg>

    <h1 class="front__title">FAMILY SERVICE COACHING</h1>
    <p class="front__question">Feeling overwhelmed?</p>
    <div class="front__pill"><span>A family service coach will work with you to:</span></div>

    <ul class="benefits benefits--left">
      <li>Feel less stressed and more in control</li>
      <li>Set goals that the whole team work towards</li>
      <li>Find and use funding wisely</li>
      <li>Build a dream team who believe in your child</li>
    </ul>
    <ul class="benefits benefits--right">
      <li>Design a therapy and education program that meets your needs</li>
      <li>Monitor and adjust the program to get best results</li>
      <li>Manage a great team who really work together</li>
    </ul>

    <div class="contact">
      <p class="contact__cta">BOOK A CHAT WITH MARA</p>
      <p class="contact__row contact__phone"><svg viewBox="0 0 16 16"><circle cx="8" cy="8" r="7" fill="none" stroke="currentColor" stroke-width="1.4"/><path d="M5.5 4.5l1.5 1.5-1 1.2c.6 1.2 1.5 2.1 2.8 2.8l1.2-1 1.5 1.5-1.2 1.2C7.8 11.5 4.5 8.2 4.3 5.7z" fill="currentColor"/></svg>0400 555 218</p>
      <p class="contact__row contact__small"><svg viewBox="0 0 16 16"><circle cx="8" cy="8" r="7" fill="none" stroke="currentColor" stroke-width="1.4"/><rect x="4" y="5.5" width="8" height="5.5" fill="none" stroke="currentColor"/><path d="M4 5.5l4 3 4-3" fill="none" stroke="currentColor"/></svg>mara@lirvo.com.au</p>
      <p class="contact__row contact__small"><svg viewBox="0 0 16 16"><circle cx="8" cy="8" r="7" fill="currentColor"/><path d="M1 8h14M8 1c-3 3.5-3 10.5 0 14M8 1c3 3.5 3 10.5 0 14" fill="none" stroke="#fff" stroke-width="1"/></svg>www.lirvo.com.au</p>
    </div>

    <div class="brand"><span class="brand__dot"></span><span class="brand__name">lirvo</span></div>
  </section>

  <section class="card card--back" aria-label="Postcard back">
    <svg class="card__art" viewBox="0 0 1040 504">
      <defs>
        <linearGradient id="puzzleTone" x1="0" y1="0" x2="1" y2="0">
          <stop offset="0" stop-color="#4a72bd" stop-opacity="0"/>
          <stop offset=".45" stop-color="#9fb6de"/>
          <stop offset=".75" stop-color="#d9a08c"/>
          <stop offset="1" stop-color="#6fae7c"/>
        </linearGradient>
        <linearGradient id="portraitTone" x1="0" y1="0" x2="0" y2="1">
          <stop offset="0" stop-color="#d6dadc"/>
          <stop offset=".55" stop-color="#b9bec1"/>
          <stop offset="1" stop-color="#2b3340"/>
        </linearGradient>
      </defs>
      <rect width="1040" height="504" fill="var(--lavender-pale)"/>
      <path d="M250,0 H1040 V118 C860,150 640,70 420,108 C340,122 290,120 250,112 Z" fill="var(--blue)"/>
      <path d="M620,0 H1040 V130 C930,150 820,140 700,120 C660,60 640,30 620,0 Z" fill="url(#puzzleTone)" role="img" aria-label="Photo of hands joining colourful puzzle pieces"/>
      <path d="M0,504 V372 C260,335 620,390 1040,365 V504 Z" fill="var(--lavender)"/>
      <path d="M0,504 V392 C260,355 620,410 1040,385 V504 Z" fill="var(--white)"/>
      <circle cx="150" cy="232" r="268" fill="var(--ring)"/>
      <circle cx="150" cy="232" r="252" fill="url(#portraitTone)" role="img" aria-label="Portrait photo of the occupational therapist and coach"/>
    </svg>

    <div class="bio">
      <p>Mara Keene is an Occupational Therapist, Professional Coach and Speaker who works with children, parents and disability service providers to achieve brilliant outcomes for children with special needs.</p>
      <p>Mara has worked with children and families for thirty years and has a great working knowledge of the complex funding and disability service systems. Together you will gain a sense of control and optimism, knowing that you are doing everything that it takes for your child.</p>
    </div>

    <div class="contact">
      <p class="contact__cta">BOOK A CHAT WITH MARA</p>
      <p class="contact__row contact__phone"><svg viewBox="0 0 16 16"><circle cx="8" cy="8" r="7" fill="none" stroke="currentColor" stroke-width="1.4"/><path d="M5.5 4.5l1.5 1.5-1 1.2c.6 1.2 1.5 2.1 2.8 2.8l1.2-1 1.5 1.5-1.2 1.2C7.8 11.5 4.5 8.2 4.3 5.7z" fill="currentColor"/></svg>0400 555 218</p>
      <p class="contact__row contact__small"><svg viewBox="0 0 16 16"><circle cx="8" cy="8" r="7" fill="none" stroke="currentColor" stroke-width="1.4"/><rect x="4" y="5.5" width="8" height="5.5" fill="none" stroke="currentColor"/><path d="M4 5.5l4 3 4-3" fill="none" stroke="currentColor"/></svg>mara@lirvo.com.au</p>
      <p class="contact__row contact__small"><svg viewBox="0 0 16 16"><circle cx="8" cy="8" r="7" fill="currentColor"/><path d="M1 8h14M8 1c-3 3.5-3 10.5 0 14M8 1c3 3.5 3 10.5 0 14" fill="none" stroke="#fff" stroke-width="1"/></svg>www.lirvo.com.au</p>
    </div>

    <div class="brand"><span class="brand__dot"></span><span class="brand__name">lirvo</span></div>
  </section>

</main>
</body>
</html>
```